SUMMIT GATHERING 2021. August 20th -22nd.

The Hosts of the conference: Grace Tabernacle-Pastors Ron n Molly ( Picture with two persons)

Guest Minister: Bishop Lorna Kiprotich. (Cedar Ridge Evangelist)

Venue:
Seattle Harborgate Lodge. 4817 North 92nd Avenue Seattle, WA 98134.

Conference times.
Friday August 20th 6pm-8:30pm
Saturday August 21st. 6pm-8:30pm

Sunday August 22nd 10am-1pm
“ CHURCH RENEWAL SERVICE”

5pm-7:30pm
TWOFOLD BLESSING SERVICE.

Target Market(s)

18-55

Industry/Entity Type

Religious/ Entertainment.

Requirements
Must have
• A highlight of the Relaunch service on Sunday August 22nd 5pm-7:30pm.
Nice to have
• Excellent ideas….

```html
<!DOCTYPE html>
<html lang="en">
<head>
<meta charset="utf-8">
<title>Summit Gathering 2021</title>
<link href="https://fonts.googleapis.com/css2?family=Oswald:wght@700&family=Cinzel:wght@400;600&family=Cabin:wght@400;600&family=Great+Vibes&display=swap" rel="stylesheet">
<style>
:root{
  --gold:#d4a52c;
  --gold-light:#f3d57a;
  --gold-dark:#9c7414;
  --plum:#3a0f3e;
  --magenta:#b3204f;
  --navy:#1a1250;
  --ink:#1d1a17;
  --white:#ffffff;
  --mist:#ececec;
  --brown:#2e1f0b;
  --grey:#8a8a8a;
}
*{margin:0;padding:0;box-sizing:border-box}
html,body{width:707px;height:1200px;overflow:hidden;background:#fff}
.flyer{position:relative;width:707px;height:1200px;overflow:hidden;font-family:"Cabin",sans-serif;color:var(--ink);
  background:radial-gradient(circle at 30% 78%,#fff 0,#f2f2f2 40%,#dedede 100%)}
.stage{position:absolute;left:0;top:0;width:707px;height:640px;
  background:linear-gradient(160deg,#5a0f3a 0%,var(--magenta) 38%,#6b1a6e 62%,var(--navy) 100%)}
.stage-glow{position:absolute;left:0;top:200px;width:420px;height:340px;
  background:radial-gradient(ellipse at 30% 50%,rgba(255,110,120,.55),transparent 70%)}
.swoosh{position:absolute;left:0;top:380px;width:707px;height:360px}
.footer-band{position:absolute;left:0;top:940px;width:707px;height:260px}
.title{position:absolute;left:0;width:100%;top:38px;text-align:center;font-family:"Oswald",sans-serif;font-weight:700;
  font-size:62px;letter-spacing:-1px;color:var(--gold-light);
  background:linear-gradient(180deg,#fbe7a0,#d4a52c 55%,#a47a18);-webkit-background-clip:text;background-clip:text;-webkit-text-fill-color:transparent}
.hosts-heading{position:absolute;left:60px;top:140px;font-family:"Cinzel",serif;color:var(--white);line-height:1}
.hosts-heading .big{font-size:54px;font-weight:400}
.hosts-heading .small{font-size:26px;margin-top:4px}
.church-band{position:absolute;left:60px;top:260px;width:368px;height:52px;
  background:linear-gradient(90deg,#b98a1e,#f0cf6d 60%,#c99a2a);color:#fff;font-size:30px;font-weight:600;
  display:flex;align-items:center;padding-left:22px}
.pastors{position:absolute;left:70px;top:312px;font-family:"Great Vibes",cursive;font-size:64px;color:#fff}
.couple-photo{position:absolute;left:395px;top:128px;width:290px;height:500px;border-radius:140px 140px 0 0;
  background:linear-gradient(180deg,#4a3a4a,#d9d4d0 45%,#3b2b2b 100%);opacity:.9}
.guest-photo{position:absolute;left:52px;top:455px;width:220px;height:220px;border-radius:50%;
  border:6px solid var(--gold);background:linear-gradient(160deg,#5b4a3a,#a08a72 55%,#5f5f5f)}
.guest-label{position:absolute;left:245px;top:495px;width:200px;height:96px;
  background:linear-gradient(90deg,#b5b5b5,#e0e0e0 50%,#9a9a9a);font-family:"Cinzel",serif;font-size:34px;line-height:.95;
  padding:12px 0 0 36px;color:var(--ink)}
.guest-name{position:absolute;left:245px;top:602px;font-size:30px;font-weight:600}
.guest-sub{position:absolute;left:246px;top:640px;font-size:16px;font-weight:600}
.pill{position:absolute;height:40px;border-radius:20px;display:flex;align-items:center;
  background:linear-gradient(90deg,var(--gold),var(--gold-light) 60%,var(--gold));font-family:"Cinzel",serif;color:#fff;font-size:28px}
.pill .icon{width:40px;height:40px;border-radius:50%;background:var(--ink);display:flex;align-items:center;justify-content:center;margin-right:12px}
.venue-pill{left:60px;top:700px;width:185px}
.times-pill{left:345px;top:700px;width:312px;font-size:25px}
.venue-text{position:absolute;left:60px;top:758px;font-size:18px;line-height:1.45}
.venue-text strong{font-weight:600}
.day{position:absolute;top:758px;width:136px;height:76px;border:1.5px solid #555;border-top:none;text-align:center}
.day .name{position:absolute;top:-14px;left:0;width:100%;font-size:22px;font-weight:600}
.day .name span{background:#efefef;padding:0 4px}
.day .date{position:absolute;top:18px;left:0;width:100%;height:28px;line-height:28px;background:linear-gradient(#9a9a9a,#6d6d6d);color:#fff;font-size:17px}
.day .time{position:absolute;top:50px;width:100%;font-size:17px}
.friday{left:368px}.saturday{left:520px}
.sunday-frame{position:absolute;left:60px;top:865px;width:590px;height:30px;border:1.5px solid #444;border-bottom:none;border-radius:6px 6px 0 0}
.sunday-line{position:absolute;left:0;width:100%;top:850px;text-align:center;font-size:29px;font-weight:600}
.sunday-line span{background:#f0f0f0;padding:0 18px}
.renewal-bar{position:absolute;left:60px;top:888px;width:590px;height:64px;border-radius:6px;
  background:linear-gradient(90deg,#a8801c,#f1d27a 50%,#b48a22);color:#fff;font-size:39px;font-weight:600;letter-spacing:1px;
  display:flex;align-items:center;justify-content:center}
.time-pill{left:60px;top:1008px;width:230px;font-family:"Cabin",sans-serif;font-size:26px;font-weight:600}
.time-pill .icon{background:#fff}
.twofold{position:absolute;left:58px;top:1060px;font-family:"Cinzel",serif;color:#fff;font-size:31px;line-height:1.15}
.divider{position:absolute;left:345px;top:1005px;width:2px;height:120px;background:#e8d7a8}
.info{position:absolute;left:364px;top:1008px;color:#fff;font-family:"Cinzel",serif;font-weight:600;font-size:20px;line-height:1.2}
.info .phone{font-family:"Cabin",sans-serif;font-size:22px;font-weight:600;display:flex;align-items:center;gap:6px;margin-top:4px}
.info .phone:first-of-type{margin-top:12px}
.church-mark{position:absolute;left:568px;top:1010px;width:100px;display:flex;flex-direction:column;align-items:center;gap:8px;color:#fff;font-size:17px;font-weight:600;text-align:center;line-height:1.1}
.church-mark .square{width:54px;height:54px;background:var(--gold)}
</style>
</head>
<body>
<div class="flyer">
  <div class="stage"></div>
  <div class="stage-glow"></div>

  <div class="couple-photo" role="img" aria-label="Photo of the host pastors standing together on stage"></div>

  <svg class="swoosh" viewBox="0 0 707 360" preserveAspectRatio="none" aria-hidden="true">
    <defs>
      <linearGradient id="gold-sweep" x1="0" x2="1">
        <stop offset="0" stop-color="#b8891e"/><stop offset=".5" stop-color="#f2d57c"/><stop offset="1" stop-color="#b68a22"/>
      </linearGradient>
    </defs>
    <path d="M0 110 C120 200 300 140 480 120 C580 110 650 100 707 130 L707 360 L0 360 Z" fill="url(#gold-sweep)"/>
    <path d="M0 140 C140 220 320 170 500 210 C600 230 660 260 707 320 L707 360 L0 360 Z" fill="#f1f1f1"/>
  </svg>

  <svg class="footer-band" viewBox="0 0 707 260" preserveAspectRatio="none" aria-hidden="true">
    <defs>
      <linearGradient id="bronze" x1="0" y1="0" x2="0" y2="1">
        <stop offset="0" stop-color="#1f1508"/><stop offset=".6" stop-color="#4a3511"/><stop offset="1" stop-color="#a97d22"/>
      </linearGradient>
    </defs>
    <path d="M0 40 C200 10 500 10 707 40 L707 260 L0 260 Z" fill="url(#bronze)"/>
  </svg>

  <h1 class="title">SUMMIT GATHERING 2021</h1>

  <div class="hosts-heading">
    <div class="big">THE HOSTS</div>
    <div class="small">OF THE CONFERENCE:</div>
  </div>
  <div class="church-band">Grace Tabernacle-Pastors</div>
  <div class="pastors">Ron n Molly</div>

  <div class="guest-photo" role="img" aria-label="Portrait photo of the guest minister"></div>
  <div class="guest-label">GUEST<br>MINISTER:</div>
  <div class="guest-name">Bishop Lorna Kiprotich</div>
  <div class="guest-sub">(Cedar Ridge Evangelist)</div>

  <div class="pill venue-pill">
    <span class="icon"><svg width="18" height="22" viewBox="0 0 18 22"><circle cx="9" cy="7" r="5" fill="none" stroke="#fff" stroke-width="2"/><path d="M9 12 V20 M4 20 H14" stroke="#fff" stroke-width="2"/></svg></span>VENUE:
  </div>
  <div class="pill times-pill">
    <span class="icon"><svg width="22" height="22" viewBox="0 0 22 22"><circle cx="11" cy="11" r="8" fill="none" stroke="#fff" stroke-width="1.6"/><path d="M11 6 V11 L14 14" stroke="#fff" stroke-width="1.6" fill="none"/></svg></span>CONFERENCE TIMES
  </div>

  <div class="venue-text">
    <strong>Seattle Harborgate Lodge.</strong><br>
    4817 North 92nd Avenue Seattle,<br>WA 98134.
  </div>

  <div class="day friday">
    <div class="name"><span>FRIDAY</span></div>
    <div class="date">August 20th</div>
    <div class="time">6pm-8:30pm</div>
  </div>
  <div class="day saturday">
    <div class="name"><span>SATURDAY</span></div>
    <div class="date">August 21st</div>
    <div class="time">6pm-8:30pm</div>
  </div>

  <div class="sunday-frame"></div>
  <div class="sunday-line"><span>Sunday August 22nd 10am-1pm</span></div>
  <div class="renewal-bar">CHURCH RENEWAL SERVICE</div>

  <div class="pill time-pill">
    <span class="icon"><svg width="22" height="22" viewBox="0 0 22 22"><circle cx="11" cy="11" r="8" fill="none" stroke="#222" stroke-width="1.6"/><path d="M11 6 V11 L14 14" stroke="#222" stroke-width="1.6" fill="none"/></svg></span>5pm-7:30pm
  </div>
  <div class="twofold">TWOFOLD<br>BLESSING SERVICE.</div>

  <div class="divider"></div>
  <div class="info">
    FOR MORE INFO<br>CALL US
    <div class="phone"><svg width="16" height="16" viewBox="0 0 16 16"><circle cx="8" cy="8" r="7" fill="none" stroke="#fff" stroke-width="1.4"/><path d="M5.5 4.5 L7 6 L6 7 C6.5 8.3 7.7 9.5 9 10 L10 9 L11.5 10.5 L10.5 11.5 C7.5 11 5 8.5 4.5 5.5 Z" fill="#fff"/></svg>0198 765 432</div>
    <div class="phone"><svg width="16" height="16" viewBox="0 0 16 16"><circle cx="8" cy="8" r="7" fill="none" stroke="#fff" stroke-width="1.4"/><path d="M5.5 4.5 L7 6 L6 7 C6.5 8.3 7.7 9.5 9 10 L10 9 L11.5 10.5 L10.5 11.5 C7.5 11 5 8.5 4.5 5.5 Z" fill="#fff"/></svg>0198 765 432</div>
  </div>

  <div class="church-mark">
    <span class="square"></span>
    <span>Grace Tabernacle</span>
  </div>
</div>
</body>
</html>
```